brainwave stimulating (brainwave entrainment ) company is searching for album cover templates

I am searching for album cover banner templates for my 4 sectors of sounds which you can see on my website.
I would like to proceed in google draw and just change the section / titel + background picture for my upcoming 30 albums.
The tracks will just be released as a digital download (3000x3000pxl)
www.lumivaleworks.com

Lumivale Works:
Tune your mind
Sounds and lights to change the states of your brainwaves patterns to access easier focus, deeper meditation or relaxation / sleep.
Modern science meets ancient wisdom.
The template should show the impression of the meditation feeling which means deep relaxation in combination with a highly awake state.

I need 1 template which contains all catepories or 4 different

Target Market(s)

Target group:
- age 20 - 40
- male & female
- mid - high income
- middle & upper class
- employees, professionals, students, digital natives
- explorer, succeder, living at the puls of time
- spiritual persons who are open to the combination with science
- yoga people who are open to the combination with science

Font styles to use
Sans Serif
Other font styles liked:
• so far I used robots. but not mandatory

Colors

Designer to choose colors to be used in the design.

Requirements
Must have
• I need 4 templates or depending on the template maybe just one if it contains all sectors and the definition comes though the sector specific names (f.e. Focus at Work (category) + deep concentration (sub category )
• The 4 sectors are
• - focus at work (red)
• - meditation & sound healing (green)
• - relex & sleep (blue)
• - guided meditations (yellow)
• I like my colors so far but they are not mandatory.
• Colors according to my website.
• www.lumivaleworks.com
• Maybe some more vibrant colors would be necessary.
• The 4 templates should contain:
• - The specific sections color
• - The templates for each sector should refer the design of the other sectors (main ID)
• - The background picture and album title should be easily changed by myself as a non professional
• - the album Titel needs to be very prominent as it is very small on all digital plattforms
• - The background picture should refer to the topic of the sector (f.e focus at work can show a computer)
• - if the background picture is a coach(guided meditations , yellow) the focus needs to be on the face of the coach. He needs to be trustworthy
• - Logo (It is not mandatory to stay with my old logo if the design of the covers may bring up a new logo)
• - the purpose of the sounds (f.e. focus at work sounds for better concentration it could show someone at at computer)
• - for guided meditations it needs to show the faces of the coaches to be trustworthy
Nice to have
• something which refers to the modern science.
• Could be some "waves" like in the banner example. Just a lot more clear
Should not have
• for guided meditations the face of the coaches need to be trustworthy.
• They shouldn't be colored in yellow f.e.
• So maybe a banner template is the best solution?

```html
<!DOCTYPE html>
<html lang="en">
<head>
<meta charset="utf-8">
<title>Meditation Sounds – Album Cover</title>
<link rel="stylesheet" href="https://fonts.googleapis.com/css2?family=Montserrat:wght@400;700&display=swap">
<style>
  :root {
    --stage-bg: #c9cccb;
    --amber-deep: #d9620a;
    --amber: #ef8f1c;
    --amber-bright: #f7b330;
    --amber-soft: #fad57a;
    --cream: #fff6dc;
    --paper: #ffffff;
    --ink: #161616;
    --ink-soft: #3a3a3a;
    --brand-slate: #8a9ba3;
  }
  * { box-sizing: border-box; margin: 0; padding: 0; }
  html, body {
    width: 1200px;
    height: 1000px;
    overflow: hidden;
    background: var(--stage-bg);
  }
  .canvas {
    position: relative;
    width: 1200px;
    height: 1000px;
  }
  .album-cover {
    position: absolute;
    left: 220px;
    top: 120px;
    width: 760px;
    height: 760px;
    background: var(--paper);
    overflow: hidden;
  }
  .cover-art {
    position: absolute;
    inset: 0;
    background:
      linear-gradient(172deg, transparent 0%, transparent 22%, rgba(217,98,10,0.45) 30%, transparent 38%, transparent 100%),
      linear-gradient(176deg, transparent 0%, transparent 44%, rgba(217,98,10,0.35) 50%, transparent 58%, transparent 100%),
      linear-gradient(180deg,
        var(--amber) 0%,
        var(--amber-bright) 28%,
        var(--amber) 48%,
        var(--amber-bright) 62%,
        var(--amber-soft) 72%,
        var(--cream) 84%,
        var(--paper) 94%);
  }
  .cover-title-block {
    position: absolute;
    left: 0;
    right: 0;
    top: 612px;
    text-align: center;
    font-family: "Montserrat", sans-serif;
    color: var(--ink);
  }
  .album-title {
    font-weight: 700;
    font-size: 27px;
    letter-spacing: 0.2px;
    line-height: 1;
  }
  .album-tagline {
    margin-top: 9px;
    font-weight: 400;
    font-size: 14px;
    color: var(--ink-soft);
    letter-spacing: 0.3px;
  }
  .brand-mark {
    position: absolute;
    left: 0;
    right: 0;
    top: 688px;
    display: flex;
    justify-content: center;
    align-items: center;
    gap: 8px;
  }
  .brand-dot {
    width: 14px;
    height: 14px;
    border-radius: 50%;
    background: var(--brand-slate);
  }
  .brand-name {
    font-family: "Montserrat", sans-serif;
    font-weight: 400;
    font-size: 13px;
    letter-spacing: 2.5px;
    text-transform: uppercase;
    color: var(--brand-slate);
  }
</style>
</head>
<body>
  <main class="canvas">
    <section class="album-cover">
      <div class="cover-art" role="img" aria-label="Abstract flowing orange and amber light waves fading to white"></div>
      <div class="cover-title-block">
        <h1 class="album-title">MEDITATION SOUNDS</h1>
        <p class="album-tagline">Meditation Made Easy</p>
      </div>
      <div class="brand-mark">
        <span class="brand-name">Lumivale Works</span>
        <span class="brand-dot"></span>
      </div>
    </section>
  </main>
</body>
</html>
```